Flyer Design

We are a new dental centre opening i would like to do a letter drop advising of our services, hours and location.

In addition to the flyer i would like to create a package for business cards, letter head and also magnets. With our colour theme being as in our logo.

Target Market(s)

Familys and adult females

Industry/Entity Type

Dental

```html
<!DOCTYPE html>
<html lang="en">
<head>
<meta charset="utf-8">
<title>Lumo Dental – Grand Opening Flyer</title>
<link rel="stylesheet" href="https://fonts.googleapis.com/css2?family=Cinzel:wght@400;700&display=swap">
<style>
  :root {
    --brand-green: #36b21c;
    --text-green: #2ca617;
    --paper: #ffffff;
    --backdrop: #eeeeee;
    --skin-light: #fbe7dc;
    --skin-mid: #f1cbb6;
    --skin-deep: #e2ab92;
    --band-text: #ffffff;
  }
  html, body {
    margin: 0;
    padding: 0;
    width: 1200px;
    height: 931px;
    overflow: hidden;
    background: var(--backdrop);
  }
  .flyer {
    position: absolute;
    left: 50px;
    top: 55px;
    width: 1100px;
    height: 820px;
    background: var(--paper);
    box-shadow: 0 4px 18px rgba(0,0,0,0.15);
    overflow: hidden;
    font-family: "Cinzel", "Times New Roman", serif;
  }
  .flyer__art {
    position: absolute;
    inset: 0 0 140px 0;
  }
  .flyer__content {
    position: absolute;
    left: 500px;
    top: 40px;
    width: 580px;
    text-align: center;
    color: var(--text-green);
  }
  .brand-name {
    font-weight: 700;
    font-size: 28px;
    line-height: 1.15;
    margin: 0 0 34px;
    color: var(--text-green);
  }
  .brand-name span { display: block; font-size: 20px; }
  .headline {
    margin: 0;
    font-weight: 400;
    font-size: 78px;
    line-height: 1;
  }
  .subheadline {
    margin: 6px 0 40px;
    font-weight: 400;
    font-size: 46px;
    line-height: 1.05;
  }
  .offer {
    margin: 0 0 26px;
    font-size: 40px;
    line-height: 1.1;
  }
  .flyer__band {
    position: absolute;
    left: 0;
    right: 0;
    bottom: 0;
    height: 140px;
    background: var(--brand-green);
    color: var(--band-text);
    text-align: center;
    display: flex;
    flex-direction: column;
    justify-content: center;
    font-size: 24px;
    line-height: 1.3;
  }
  .flyer__band p { margin: 0; }
</style>
</head>
<body>
  <article class="flyer">
    <svg class="flyer__art" width="1100" height="680" viewBox="0 0 1100 680" aria-hidden="false">
      <defs>
        <linearGradient id="skinTone" x1="0" y1="0" x2="1" y2="1">
          <stop offset="0" stop-color="var(--skin-light)"/>
          <stop offset="0.55" stop-color="var(--skin-mid)"/>
          <stop offset="1" stop-color="var(--skin-deep)"/>
        </linearGradient>
      </defs>
      <rect class="portrait-photo" x="0" y="0" width="720" height="680" fill="url(#skinTone)" role="img" aria-label="Photo of a smiling young woman with white teeth"/>
      <path class="content-panel" d="M560 0 H1100 V680 H300 C360 560 470 470 520 330 C555 230 540 110 560 0 Z" fill="var(--paper)"/>
    </svg>

    <div class="flyer__content">
      <p class="brand-name">Lumo<span>Medical Centre</span></p>
      <h1 class="headline">Lumo Dental</h1>
      <h2 class="subheadline">Grand Opening 2014</h2>
      <p class="offer">Same day urgent<br>care appointment</p>
      <p class="offer">Opening Special Sports<br>Mouthguards $80.00</p>
    </div>

    <footer class="flyer__band">
      <p>located within the newly renovated</p>
      <p>Lumo Medical Centre 452 Harbour View Rd Kensington</p>
      <p>Phone: 9000 1234 for an appointment</p>
    </footer>
  </article>
</body>
</html>
```